Business Card Design for New Game Studio

We need a business card design. We are a new company developing innovative mobile and platform games.

I would like to see very innovative design thats brings out the company's goal and direction.

My Company's goal and direction is to "Evolve the way of gaming, Bring fun and entertainment to all gamers"

Please do use our company logo which I have attached to be included in the design.

Please put in details for name, title, contacts etc ... be creative !!!

Reason: Company logo redesign. Awaiting it. Thanks

Hi all Please do wait for my updated company logo. Thanks

Reason: Still waiting on new company logo. Thanks all

Hi All Designers .... Sorry for the long wait... Please see the new file for my new company logo uploaded. Waiting to see all your creative design. Cheers

Hi All .... Please do not just mass send a whole bunch of similar designs .... Would like to see quality instead of quantity Cheers

Entertainment

```html
<!DOCTYPE html>
<html lang="en">
<head>
<meta charset="utf-8">
<title>Kestrel Games – Business Card</title>
<link href="https://fonts.googleapis.com/css2?family=Tinos:wght@400;700&display=swap" rel="stylesheet">
<style>
  :root {
    --backdrop: #d9d9d9;
    --card: #3c3c3e;
    --lime: #d3df1e;
    --ink: #f2f2f2;
    --muted: #bdbdbd;
  }
  * { margin: 0; padding: 0; box-sizing: border-box; }
  html, body { width: 1200px; height: 900px; overflow: hidden; }
  body {
    background: var(--backdrop);
    font-family: "Tinos", "Times New Roman", serif;
    display: flex;
    align-items: center;
    justify-content: center;
    gap: 40px;
  }
  .card {
    position: relative;
    width: 540px;
    height: 310px;
    background: var(--card);
    color: var(--ink);
    box-shadow: 0 8px 22px rgba(0,0,0,0.35);
    overflow: hidden;
  }
  /* Front */
  .accent-bar { position: absolute; background: var(--lime); }
  .accent-bar--left { left: 12px; top: 150px; width: 24px; height: 110px; }
  .accent-bar--top { right: 20px; top: 0; width: 24px; height: 105px; }
  .person { position: absolute; top: 34px; left: 270px; text-align: left; }
  .person__name { font-size: 17px; font-weight: 700; letter-spacing: 1px; line-height: 1; }
  .person__title { font-size: 11px; letter-spacing: 2.5px; margin-top: 2px; }
  .brand {
    position: absolute;
    display: flex;
    align-items: center;
    gap: 10px;
    color: var(--lime);
    font-weight: 700;
    white-space: nowrap;
  }
  .brand__mark { background: var(--lime); flex: none; }
  .card--front .brand { left: 72px; top: 120px; font-size: 24px; }
  .card--front .brand__mark { width: 22px; height: 22px; }
  .contacts {
    position: absolute;
    left: 70px; top: 200px;
    width: 225px;
    list-style: none;
    text-align: right;
    font-size: 13px;
  }
  .contacts li { display: flex; justify-content: flex-end; align-items: center; gap: 8px; height: 22px; }
  .contacts svg, .address svg { width: 15px; height: 15px; flex: none; }
  .divider { position: absolute; left: 305px; top: 180px; width: 1px; height: 90px; background: var(--muted); }
  .address { position: absolute; left: 318px; top: 182px; display: flex; align-items: center; gap: 8px; font-size: 13px; }
  /* Back */
  .card--back { display: flex; align-items: center; justify-content: center; }
  .card--back .brand { position: static; font-size: 40px; gap: 14px; }
  .card--back .brand__mark { width: 34px; height: 34px; }
</style>
</head>
<body>
  <section class="card card--front">
    <div class="accent-bar accent-bar--left"></div>
    <div class="accent-bar accent-bar--top"></div>
    <div class="person">
      <p class="person__name">YOUR NAME</p>
      <p class="person__title">Designation</p>
    </div>
    <div class="brand"><span class="brand__mark"></span><span>Kestrel Games</span></div>
    <ul class="contacts">
      <li>0000000000
        <svg viewBox="0 0 16 16" fill="none" stroke="#f2f2f2" stroke-width="1.2"><circle cx="8" cy="8" r="7"/><path d="M5.5 4.5l1.5 2-1 1c.6 1.2 1.4 2 2.5 2.5l1-1 2 1.5-1 1.5c-3 0-6-3-6-6z" fill="#f2f2f2" stroke="none"/></svg></li>
      <li>your email@mail.com
        <svg viewBox="0 0 16 16" fill="none" stroke="#f2f2f2" stroke-width="1.2"><circle cx="8" cy="8" r="7"/><rect x="4.5" y="5.5" width="7" height="5"/><path d="M4.5 5.5L8 8.5l3.5-3"/></svg></li>
      <li>Your website.com
        <svg viewBox="0 0 16 16" fill="none" stroke="#f2f2f2" stroke-width="1.2"><circle cx="8" cy="8" r="7"/><circle cx="8" cy="8" r="4"/><path d="M4 8h8M8 4v8"/></svg></li>
    </ul>
    <div class="divider"></div>
    <div class="address">
      <svg viewBox="0 0 16 16" fill="none" stroke="#f2f2f2" stroke-width="1.2"><circle cx="8" cy="8" r="7"/><path d="M4.5 8.5L8 5l3.5 3.5M5.5 7.5V11h5V7.5"/></svg>
      <span>Your Address</span>
    </div>
  </section>

  <section class="card card--back">
    <div class="brand"><span class="brand__mark"></span><span>Kestrel Games</span></div>
  </section>
</body>
</html>
```